We are an online mail order nursery selling live plants who needs a 1 page landing page for an upcom

We are opening a new sister site to our main site. The new site is membership based. We need a landing page for an email campaign that is both attention grabbing and simply luring the customer to click on the learn more about Membership Page : http://www.thefernguild.com/pages/membership-info
The landing page will need to have space reserved for a white board presentation. I have attached the video below. The vid will be hosted on You tube so we should be able to use the iframe / embed technique. Again our goal is to funnel the customer to http://www.thefernguild.com/pages/membership-info where they can get more details.

Target Market(s)

Home owners between the age of 35 and 65 - gardening enthusiast

Industry/Entity Type

Campaign

Number of Pages Required

1 page

Font styles to use
Sans Serif

Requirements
Must have
• space to embed white board video

```html
<!DOCTYPE html>
<html lang="en">
<head>
<meta charset="utf-8">
<title>The Fern Guild – Online Mail Order Nursery</title>
<link href="https://fonts.googleapis.com/css2?family=Roboto:wght@300;400;500;700&family=Roboto+Condensed:wght@400;500&family=Cinzel:wght@500&display=swap" rel="stylesheet">
<style>
:root{
  --green-dark:#0c4a26;
  --green-brand:#1f6b34;
  --green-lime:#8cc63f;
  --ink:#222;
  --text:#333;
  --footer:#262626;
  --panel:#fbf7f1;
  --line:#cfcfcf;
}
*{box-sizing:border-box;margin:0;padding:0}
html,body{width:1200px;height:1077px;overflow:hidden;background:#fff;font-family:"Roboto",sans-serif;color:var(--text)}
a{text-decoration:none;color:inherit}
.page{position:relative;width:1200px;height:1077px}

/* header */
.site-header{position:absolute;top:0;left:0;width:1200px;height:117px;background:#fff}
.brand{position:absolute;left:100px;top:36px;display:flex;align-items:center;gap:12px}
.brand-mark{width:62px;height:40px;border-radius:50%;background:var(--green-brand)}
.brand-name{font-family:"Cinzel",serif;font-size:29px;line-height:1;color:var(--green-brand);border-left:1px solid #bbb;padding-left:10px}
.brand-name small{display:block;font-size:14px;letter-spacing:1px}
.cart{position:absolute;left:820px;top:15px;font-size:12px;color:#444;display:flex;align-items:center;gap:8px}
.account{position:absolute;left:922px;top:0;width:179px;height:43px;background:var(--green-lime);clip-path:polygon(0 0,100% 0,88% 100%,12% 100%);color:#fff;font-size:13px;font-weight:500;display:flex;align-items:center;justify-content:center;gap:12px}
.main-nav{position:absolute;right:98px;top:74px;display:flex;align-items:center;font-size:13px;font-weight:500;color:#333;text-transform:uppercase}
.main-nav a{padding:0 9px;position:relative}
.main-nav a+a::before{content:"|";position:absolute;left:-3px;color:#555}
.main-nav .active{color:var(--green-brand)}
.main-nav .active::after{content:"";position:absolute;left:2px;right:2px;top:36px;height:4px;background:var(--green-lime)}
.main-nav svg{margin-left:8px}

/* hero */
.hero{position:absolute;top:117px;left:0;width:1200px;height:476px;background:radial-gradient(ellipse at 45% 45%,#6b5a45 0%,#3f3a26 30%,#2c4620 60%,#1d3214 100%)}
.hero-copy{position:absolute;left:95px;top:145px;width:440px;color:#fff}
.hero-copy h1{font-family:"Roboto Condensed",sans-serif;font-weight:500;font-size:40px;letter-spacing:-.5px;line-height:1}
.hero-copy p{margin-top:18px;font-size:13px;font-weight:300;line-height:20.5px}
.btn{display:inline-block;background:var(--green-lime);color:#fff;font-weight:500;border-radius:3px;text-align:center}
.hero-copy .btn{margin-top:22px;width:155px;height:59px;line-height:59px;font-size:17px}
.dots{position:absolute;left:559px;top:426px;display:flex;gap:19px}
.dots span{width:15px;height:15px;border-radius:50%;background:#fff}
.dots span.on{background:var(--green-lime)}

.quick-contact{position:absolute;left:850px;top:61px;width:251px;height:354px;background:var(--panel)}
.quick-contact h2{height:62px;background:var(--green-dark);color:#fff;font-weight:400;font-size:22px;text-align:center;line-height:62px}
.quick-contact form{padding:16px 12px 0}
.field{height:39px;border:1px solid var(--line);background:#fff;margin-bottom:5px;font-size:12.5px;color:#555;padding:12px 8px}
.field.msg{height:62px;padding-top:7px}
.submit{display:block;margin:22px auto 0;width:124px;height:41px;background:var(--ink);color:#fff;border:0;border-radius:6px;font:500 13px "Roboto",sans-serif;letter-spacing:.3px}

/* intro */
.video-frame{position:absolute;left:100px;top:637px;width:499px;height:280px;border:1px solid #ccc;padding:3px;background:#fff;box-shadow:0 24px 18px -18px rgba(0,0,0,.3)}
.video{width:100%;height:100%;background:linear-gradient(#7a7a7a,#6a6a6a);position:relative}
.video .play{position:absolute;left:50%;top:46%;transform:translate(-50%,-50%)}
.video .bar{position:absolute;left:12px;right:12px;bottom:10px;display:flex;align-items:center;gap:14px}
.video .track{flex:1;height:3px;background:#999}
.video .track i{display:block;width:45%;height:100%;background:#1aa8e8}

.referral{position:absolute;left:650px;top:634px;width:451px}
.referral h2{font-size:21.5px;font-weight:500;color:#111;letter-spacing:-.2px}
.referral p{margin-top:16px;font-size:11.6px;line-height:20.6px;color:#333;text-align:justify}
.referral .btn{margin-top:20px;width:114px;height:45px;line-height:45px;font-size:14px}

/* footer */
.site-footer{position:absolute;left:0;top:962px;width:1200px;height:115px;background:var(--footer);color:#ddd}
.copyright{position:absolute;left:104px;top:44px;font-size:13px;font-weight:300}
.social{position:absolute;left:918px;top:44px;display:flex;gap:34px}
.social a{width:20px;height:20px;border-radius:50%;background:#eee}
</style>
</head>
<body>
<div class="page">

  <header class="site-header">
    <a class="brand" href="http://www.thefernguild.com/pages/membership-info">
      <span class="brand-mark"></span>
      <span class="brand-name"><small>THE</small>FERN GUILD</span>
    </a>
    <div class="cart">
      <svg width="16" height="14" viewBox="0 0 16 14"><path d="M1 1h3l2 8h8l1-6H5" fill="none" stroke="#8cc63f" stroke-width="2"/><circle cx="7" cy="12" r="1.5" fill="#8cc63f"/><circle cx="13" cy="12" r="1.5" fill="#8cc63f"/></svg>
      (0) time
    </div>
    <div class="account"><a href="#">LOGIN</a><span>|</span><a href="#">REGISTER</a></div>
    <nav class="main-nav">
      <a class="active" href="#">Home</a><a href="#">Catalog</a><a href="#">Blog</a><a href="#">About Us</a><a href="#">Flash Deals</a><a href="http://www.thefernguild.com/pages/membership-info">Membership</a><a href="#">Contact</a>
      <svg width="17" height="17" viewBox="0 0 17 17"><circle cx="7" cy="7" r="5.5" fill="none" stroke="#1f6b34" stroke-width="2.5"/><path d="M11 11l5 5" stroke="#1f6b34" stroke-width="2.5"/></svg>
    </nav>
  </header>

  <section class="hero" role="img" aria-label="Photo of cupped hands holding soil with a young seedling">
    <div class="hero-copy">
      <h1>ONLINE MAIL ORDER NURSERY</h1>
      <p>When you are planting a perennial border that is 5 foot wide and 40 feet long and placing the plants in groups of 3 and 5 those $14 to $20 dollar plants that most mail order companies offer can break the bank.</p>
      <a class="btn" href="http://www.thefernguild.com/pages/membership-info">ENTER NOW</a>
    </div>
    <div class="dots"><span></span><span class="on"></span><span></span></div>
    <aside class="quick-contact">
      <h2>QUICK CONTACT</h2>
      <form>
        <div class="field">Name :</div>
        <div class="field">Email :</div>
        <div class="field">Mobile :</div>
        <div class="field msg">Message :</div>
        <button class="submit" type="button">SUBMIT NOW!</button>
      </form>
    </aside>
  </section>

  <div class="video-frame">
    <div class="video" role="img" aria-label="Embedded whiteboard presentation video about membership savings">
      <svg class="play" width="64" height="64" viewBox="0 0 64 64"><circle cx="32" cy="32" r="31" fill="rgba(255,255,255,.35)"/><path d="M25 19l21 13-21 13z" fill="#fff"/></svg>
      <div class="bar">
        <svg width="10" height="10" viewBox="0 0 10 10"><rect x="1" y="0" width="3" height="10" fill="#fff"/><rect x="6" y="0" width="3" height="10" fill="#fff"/></svg>
        <div class="track"><i></i></div>
      </div>
    </div>
  </div>

  <section class="referral">
    <h2>When you refer a friend we send them an email</h2>
    <p>All gardeners know that 'dream' gardens like the ones you see in magazines are expensive. When you are planting a perennial border that is 5 foot wide and 40 feet long and placing the plants in groups of 3 and 5 those $14 to $20 dollar plants that most mail order companies offer can break the bank and result in disappointment because you tried to use less plants to save money. With our $30 per year Gold Membership you are entitled to a 30% discount on top of a 50% discount on all items in the catalog with every purchase.... no more waiting for coupon offers. You can even participate in weekly flash sales where we liquidate inventory for other nurseries and pick up some items below wholesale. Join now and get started on that dream garden.</p>
    <a class="btn" href="http://www.thefernguild.com/pages/membership-info">ENTER NOW</a>
  </section>

  <footer class="site-footer">
    <p class="copyright">© 2016 thefernguild.com - All Rights Reseverd</p>
    <div class="social"><a href="#" aria-label="Social link"></a><a href="#" aria-label="Social link"></a><a href="#" aria-label="Social link"></a><a href="#" aria-label="News feed"></a></div>
  </footer>

</div>
</body>
</html>
```